RLTP Business Card Design

I have a rough idea of the design / layout of the company business card but need help in finalizing the design and quality.

I'm looking for the card to be stand out, but simple, on the front with clear detail on the back with space for some one to write any other detail they need onto the card. The rough draft includes the crinkled graph paper back ground which I quite like for the front.

I will need the card design completed and ready to print in Australian business card standard sizes. This includes detail on all colors, fonts and type faces used as well as copy of the original for editing (inserting other employee details).

I have included the company logo and a rough draft of the card, including the graphic I would like to use for the back ground on the front, I am not sure that the graphic is any good for printing, not the highest res.

Thanks,

Owen

```html
<!DOCTYPE html>
<html lang="en">
<head>
<meta charset="utf-8">
<title>RLTP Business Card – Front</title>
<link rel="stylesheet" href="https://fonts.googleapis.com/css2?family=Saira+Condensed:wght@700&family=Saira:wght@800&family=Didact+Gothic&display=swap">
<style>
  :root {
    --backdrop: #e9e9e9;
    --card-white: #ffffff;
    --ink-black: #050505;
    --banner-grey: #6a6a6a;
    --panel-light: #f2f2f2;
    --panel-mid: #d6d6d6;
    --text-white: #ffffff;
  }
  * { margin: 0; padding: 0; box-sizing: border-box; }
  html, body { width: 1200px; height: 900px; overflow: hidden; }
  body {
    background: var(--backdrop);
    display: flex;
    align-items: center;
    justify-content: center;
  }
  .business-card {
    position: relative;
    width: 1000px;
    height: 611px;
    background: var(--card-white);
    border: 6px solid var(--ink-black);
    box-shadow: 0 10px 30px rgba(0,0,0,0.18);
    overflow: hidden;
  }
  .card-shapes { position: absolute; inset: 0; width: 100%; height: 100%; }
  .holder-name {
    position: absolute;
    left: 110px;
    top: 32px;
    font-family: "Saira Condensed", sans-serif;
    font-weight: 700;
    font-size: 72px;
    letter-spacing: 1px;
    color: var(--text-white);
    line-height: 1;
  }
  .holder-role {
    position: absolute;
    right: 42px;
    top: 232px;
    font-family: "Didact Gothic", sans-serif;
    font-size: 26px;
    letter-spacing: 2px;
    color: var(--text-white);
  }
  .contact-list {
    position: absolute;
    left: 28px;
    top: 178px;
    list-style: none;
    font-family: "Didact Gothic", sans-serif;
    font-size: 27px;
    color: var(--text-white);
  }
  .contact-item {
    display: flex;
    align-items: center;
    gap: 14px;
    height: 50px;
  }
  .contact-icon {
    width: 26px; height: 26px;
    flex: none;
  }
  .brand-mark {
    position: absolute;
    left: 560px;
    top: 360px;
    display: flex;
    align-items: center;
    gap: 18px;
    font-family: "Saira", sans-serif;
    font-weight: 800;
    font-size: 120px;
    line-height: 1;
    color: var(--ink-black);
  }
  .brand-dot {
    width: 26px; height: 26px;
    background: var(--ink-black);
    flex: none;
  }
</style>
</head>
<body>
  <div class="business-card">
    <svg class="card-shapes" viewBox="0 0 988 599" preserveAspectRatio="none" aria-hidden="true">
      <defs>
        <linearGradient id="logo-panel-fill" x1="0" y1="0" x2="1" y2="1">
          <stop offset="0" stop-color="var(--panel-mid)"/>
          <stop offset="0.55" stop-color="var(--panel-light)"/>
          <stop offset="1" stop-color="#fafafa"/>
        </linearGradient>
      </defs>
      <!-- name banner -->
      <polygon points="80,18 520,18 560,148 80,148 80,18" fill="var(--banner-grey)" transform="translate(0,0)"/>
      <polygon points="80,18 520,18 580,148 80,148" fill="var(--banner-grey)"/>
      <!-- contact panel -->
      <polygon points="0,168 450,168 470,480 0,480" fill="var(--ink-black)"/>
      <!-- role band -->
      <polygon points="470,200 988,200 988,312 500,312" fill="var(--ink-black)"/>
      <!-- logo panel -->
      <polygon points="492,330 988,330 988,599 508,599" fill="url(#logo-panel-fill)"/>
    </svg>

    <div class="holder-name">PETER LORNE</div>
    <div class="holder-role">FINANCIAL ADVISOR</div>

    <ul class="contact-list">
      <li class="contact-item">
        <svg class="contact-icon" viewBox="0 0 26 26"><circle cx="13" cy="13" r="13" fill="#fff"/><path d="M9 7c1 0 2 3 2 3l-1 1c0 2 3 5 5 5l1-1s3 1 3 2-2 2-3 2C11 19 7 15 7 9c0-1 1-2 2-2z" fill="#050505"/></svg>
        <span>012 345 6789</span>
      </li>
      <li class="contact-item">
        <svg class="contact-icon" viewBox="0 0 26 26"><circle cx="13" cy="13" r="13" fill="#fff"/><rect x="9" y="6" width="8" height="14" rx="1.5" fill="#050505"/><rect x="10.5" y="8" width="5" height="9" fill="#fff"/></svg>
        <span>012 345 6789</span>
      </li>
      <li class="contact-item">
        <svg class="contact-icon" viewBox="0 0 26 26"><circle cx="13" cy="13" r="13" fill="#fff"/><rect x="6" y="8" width="14" height="10" fill="#050505"/><path d="M6 8l7 6 7-6" stroke="#fff" stroke-width="1.3" fill="none"/></svg>
        <span>urname@email.com</span>
      </li>
      <li class="contact-item">
        <svg class="contact-icon" viewBox="0 0 26 26"><circle cx="13" cy="13" r="13" fill="#fff"/><circle cx="13" cy="13" r="7" stroke="#050505" stroke-width="1.6" fill="none"/><path d="M6 13h14M13 6c-3 4-3 10 0 14M13 6c3 4 3 10 0 14" stroke="#050505" stroke-width="1.3" fill="none"/></svg>
        <span>www.urwebsitename.com</span>
      </li>
      <li class="contact-item">
        <svg class="contact-icon" viewBox="0 0 26 26"><circle cx="13" cy="13" r="13" fill="#fff"/><path d="M13 5a5 5 0 0 1 5 5c0 4-5 10-5 10s-5-6-5-10a5 5 0 0 1 5-5z" fill="#050505"/><circle cx="13" cy="10" r="2" fill="#fff"/></svg>
        <span>27 Harbour Lane, Level 4, Kelby</span>
      </li>
    </ul>

    <div class="brand-mark">
      <span class="brand-dot"></span>
      <span class="brand-name">RLTP</span>
    </div>
  </div>
</body>
</html>
```